2m x 3m Trade Show Booth Design

We have a Hospitality Trade Show with a 2m x 3m spot. Two side walls of 2m and one back wall of 3m. Need artwork to be printed on vinyl and attached. Please see attached docs for existing media, logos, etc

```html
<!DOCTYPE html>
<html lang="en">
<head>
<meta charset="utf-8">
<title>TableMedic – Trade Show Booth Artwork</title>
<link href="https://fonts.googleapis.com/css2?family=Poppins:wght@400;500;600;700;800&display=swap" rel="stylesheet">
<style>
  :root{
    --navy:#163a63;
    --navy-deep:#0f2d52;
    --teal:#3fb3ba;
    --teal-bright:#24b0b5;
    --white:#ffffff;
    --stage:#e6e7e9;
    --placeholder-a:#2a8f97;
    --placeholder-b:#1d4a6e;
  }
  *{box-sizing:border-box;margin:0;padding:0}
  html,body{width:1194px;height:1200px;overflow:hidden}
  body{font-family:"Poppins",sans-serif;background:var(--white);color:var(--navy-deep);position:relative}

  .title-bar{position:absolute;left:0;top:0;width:1194px;height:245px;background:var(--white)}
  .brand{position:absolute;left:164px;top:62px;width:410px}
  .brand-name{font-weight:700;font-size:78px;line-height:1;letter-spacing:-2px;color:var(--navy-deep)}
  .brand-rule{height:2px;background:var(--teal-bright);margin-top:12px}
  .brand-tag{font-weight:500;font-size:20px;margin-top:6px;color:var(--navy-deep);white-space:nowrap}
  .title-divider{position:absolute;left:618px;top:42px;width:4px;height:158px;background:var(--navy-deep)}
  .project-title{position:absolute;left:668px;top:62px;font-size:48px;line-height:1.25;color:var(--navy-deep)}
  .project-title strong{font-weight:800;display:block}
  .project-title span{font-weight:500;display:block}

  .stage{position:absolute;left:0;top:245px;width:1194px;height:955px;background:var(--stage)}

  .panel{position:absolute;overflow:hidden}
  .fascia-tagline{left:60px;top:45px;width:360px;height:120px;background:var(--teal);display:flex;align-items:center;gap:20px;padding-left:46px}
  .fascia-tagline p{color:var(--white);font-weight:600;font-size:18px;line-height:1.2}
  .fascia-brand{left:420px;top:45px;width:714px;height:120px;background:var(--navy);display:flex;flex-direction:column;justify-content:center;align-items:center}
  .fascia-brand .swoosh{position:absolute;right:-40px;top:-30px;width:120px;height:180px;border-radius:50%;background:var(--teal)}

  .logo-on-dark .brand-name{color:var(--white)}
  .logo-on-dark .brand-rule{background:var(--teal-bright)}
  .logo-on-dark .brand-tag{color:var(--white)}
  .fascia-brand .brand-name{font-size:50px;letter-spacing:-1px}
  .fascia-brand .brand-rule{margin-top:6px}
  .fascia-brand .brand-tag{font-size:14px;margin-top:4px}

  .side-wall{left:60px;top:185px;width:300px;height:440px;background:var(--navy)}
  .side-wall .upper{height:250px;background:var(--teal)}
  .side-wall .contact{padding:36px 0 0 46px;color:var(--white)}
  .contact-line{display:flex;align-items:center;gap:10px}
  .contact-phone{font-weight:600;font-size:26px}
  .contact-web{font-weight:500;font-size:17px;margin-top:8px}

  .back-wall{left:380px;top:185px;width:754px;height:440px;background:var(--navy)}
  .back-wall .sweep{position:absolute;left:-60px;top:220px;width:620px;height:90px;border-radius:50%;border-top:10px solid #1d5a80}
  .headline{position:absolute;left:40px;top:52px;font-weight:700;font-size:30px;line-height:1.3;color:var(--teal)}
  .subline{position:absolute;left:40px;top:142px;font-weight:600;font-size:22px;color:var(--white)}
  .services{position:absolute;left:40px;top:250px;display:grid;grid-template-columns:150px 150px;row-gap:18px;column-gap:16px}
  .service{display:flex;align-items:center;gap:9px;color:var(--white);font-weight:500;font-size:11px;line-height:1.25}
  .service svg{flex:none}
  .strip{position:absolute;left:0;bottom:0;width:754px;height:48px;background:var(--teal);color:var(--white);font-weight:600;font-size:17px;display:flex;align-items:center;padding-left:40px}
  .mascot{position:absolute;right:0;top:30px;width:330px;height:362px;background:linear-gradient(160deg,var(--placeholder-a),var(--placeholder-b));border-radius:160px 160px 0 0}

  .counter{left:262px;top:650px;width:670px;height:250px;background:var(--navy);border-radius:0 0 40px 40px;display:flex;flex-direction:column;justify-content:center;padding-left:70px}
  .counter .brand-name{font-size:76px}
  .counter .brand-rule{width:470px}
  .counter .brand-tag{font-size:20px}
</style>
</head>
<body>
  <header class="title-bar">
    <div class="brand">
      <div class="brand-name">TableMedic</div>
      <div class="brand-rule"></div>
      <div class="brand-tag">Hospitality IT, POS &amp; Network Specialists</div>
    </div>
    <div class="title-divider"></div>
    <h1 class="project-title"><strong>TRADE SHOW</strong><span>BOOTH DESIGN</span></h1>
  </header>

  <main class="stage">
    <section class="panel fascia-tagline">
      <svg width="50" height="50" viewBox="0 0 50 50" aria-hidden="true">
        <circle cx="25" cy="25" r="21" fill="none" stroke="#fff" stroke-width="6"/>
        <path d="M15 25l7 7 14-15" fill="none" stroke="#fff" stroke-width="6" stroke-linecap="round" stroke-linejoin="round"/>
      </svg>
      <p>Fixing Today.<br>Helping<br>Tomorrow.</p>
    </section>

    <section class="panel fascia-brand logo-on-dark">
      <div class="swoosh"></div>
      <div class="brand-name">TableMedic</div>
      <div class="brand-rule" style="width:330px"></div>
      <div class="brand-tag">Hospitality IT, POS &amp; Network Specialists</div>
    </section>

    <section class="panel side-wall">
      <div class="upper"></div>
      <div class="contact">
        <div class="contact-line contact-phone">
          <svg width="18" height="18" viewBox="0 0 24 24" aria-hidden="true"><path d="M6.6 10.8a15 15 0 006.6 6.6l2.2-2.2c.3-.3.7-.4 1-.2 1.1.4 2.3.6 3.6.6.6 0 1 .4 1 1V20c0 .6-.4 1-1 1A17 17 0 013 4c0-.6.4-1 1-1h3.5c.6 0 1 .4 1 1 0 1.3.2 2.5.6 3.6.1.3 0 .7-.2 1z" fill="#3fb3ba"/></svg>
          1300 555 018
        </div>
        <div class="contact-line contact-web">
          <svg width="18" height="18" viewBox="0 0 24 24" aria-hidden="true"><circle cx="12" cy="12" r="9" fill="none" stroke="#3fb3ba" stroke-width="2.4"/><path d="M3 12h18M12 3c3 3 3 15 0 18M12 3c-3 3-3 15 0 18" fill="none" stroke="#3fb3ba" stroke-width="2"/></svg>
          tablemedic.com.au
        </div>
      </div>
    </section>

    <section class="panel back-wall">
      <div class="sweep"></div>
      <h2 class="headline">YOUR HOSPITALITY<br>TECH DOCTOR.</h2>
      <p class="subline">FAST. LOCAL. RELIABLE.</p>
      <ul class="services">
        <li class="service">
          <svg width="26" height="26" viewBox="0 0 26 26" aria-hidden="true"><circle cx="13" cy="13" r="12" fill="none" stroke="#3fb3ba" stroke-width="2"/><rect x="9" y="7" width="8" height="12" rx="1.5" fill="none" stroke="#fff" stroke-width="1.6"/></svg>
          <span>POS &amp; EFTPOS<br>support</span>
        </li>
        <li class="service">
          <svg width="26" height="26" viewBox="0 0 26 26" aria-hidden="true"><circle cx="13" cy="13" r="12" fill="none" stroke="#3fb3ba" stroke-width="2"/><path d="M7 11a9 9 0 0112 0M9 14a5.5 5.5 0 018 0" fill="none" stroke="#fff" stroke-width="1.6" stroke-linecap="round"/><circle cx="13" cy="17.5" r="1.4" fill="#fff"/></svg>
          <span>Network &amp;<br>Wi‑Fi repairs</span>
        </li>
        <li class="service">
          <svg width="26" height="26" viewBox="0 0 26 26" aria-hidden="true"><circle cx="13" cy="13" r="12" fill="none" stroke="#3fb3ba" stroke-width="2"/><rect x="7.5" y="10" width="11" height="6" rx="1" fill="none" stroke="#fff" stroke-width="1.6"/><path d="M9.5 10V7h7v3M9.5 16v3h7v-3" fill="none" stroke="#fff" stroke-width="1.6"/></svg>
          <span>Thermal<br>printer fixes</span>
        </li>
        <li class="service">
          <svg width="26" height="26" viewBox="0 0 26 26" aria-hidden="true"><circle cx="13" cy="13" r="12" fill="none" stroke="#3fb3ba" stroke-width="2"/><path d="M7 8h12v8h-7l-3 3v-3H7z" fill="none" stroke="#fff" stroke-width="1.6" stroke-linejoin="round"/></svg>
          <span>Hospitality IT<br>consulting</span>
        </li>
      </ul>
      <div class="mascot" role="img" aria-label="Illustrated friendly technician in a teal cap and jacket holding a card payment terminal"></div>
      <div class="strip">Onsite &amp; Remote Troubleshooting</div>
    </section>

    <section class="panel counter logo-on-dark">
      <div class="brand-name">TableMedic</div>
      <div class="brand-rule"></div>
      <div class="brand-tag">Hospitality IT, POS &amp; Network Specialists</div>
    </section>
  </main>
</body>
</html>
```